Business Card Design Project

We consult with hotels on setting rates and maximizing a revenue strategy

Industry/Entity Type

Business

Contact Information for Business Card

I am not sure what I want. Our company offers high level consulting to hotels around the country but we are also laid back. I would like something that is professional but also shows the laid back side

```html
<!DOCTYPE html>
<html lang="en">
<head>
<meta charset="utf-8">
<title>Harborline Business Card</title>
<link rel="stylesheet" href="https://fonts.googleapis.com/css2?family=Open+Sans:wght@400;700;800&display=swap">
<style>
  :root {
    --backdrop: #2b2b2d;
    --card-light: #ffffff;
    --card-dark: #140c0a;
    --ink-brown: #2a1a15;
    --teal: #2e9488;
    --on-dark: #f2f2f2;
    --muted-on-dark: #c9c9c9;
  }
  * { box-sizing: border-box; margin: 0; padding: 0; }
  html, body { width: 1200px; height: 1000px; overflow: hidden; }
  body {
    background: var(--backdrop);
    font-family: "Open Sans", Arial, sans-serif;
    position: relative;
  }
  .card {
    position: absolute;
    left: 280px;
    width: 640px;
    height: 366px;
    box-shadow: 0 12px 30px rgba(0,0,0,0.5);
  }
  .card--front { top: 90px; background: var(--card-light); }
  .card--back { top: 544px; background: var(--card-dark); color: var(--on-dark); }

  /* Front */
  .front-brand {
    position: absolute;
    left: 100px;
    top: 120px;
    display: flex;
    align-items: center;
    gap: 18px;
  }
  .brand-square {
    width: 56px; height: 56px;
    background: var(--teal);
  }
  .front-brand .brand-name {
    font-weight: 800;
    font-size: 56px;
    letter-spacing: 1px;
    color: var(--ink-brown);
    line-height: 1;
  }
  .front-tagline {
    position: absolute;
    left: 174px;
    top: 186px;
    background: var(--ink-brown);
    color: #fff;
    font-weight: 700;
    font-size: 17px;
    padding: 3px 14px;
  }
  .front-website {
    position: absolute;
    left: 100px;
    top: 236px;
    font-weight: 800;
    font-size: 36px;
    color: var(--ink-brown);
  }

  /* Back */
  .back-brand {
    position: absolute;
    left: 40px;
    top: 44px;
  }
  .back-brand .brand-row { display: flex; align-items: center; gap: 10px; }
  .back-brand .brand-square { width: 30px; height: 30px; }
  .back-brand .brand-name {
    font-weight: 800;
    font-size: 30px;
    color: var(--on-dark);
    line-height: 1;
  }
  .back-brand .brand-tagline {
    font-weight: 700;
    font-size: 11px;
    color: var(--on-dark);
    margin: 4px 0 0 40px;
  }
  .person {
    position: absolute;
    right: 46px;
    top: 110px;
    text-align: right;
  }
  .person-name { font-size: 34px; font-weight: 400; line-height: 1.1; }
  .person-title { font-size: 14px; color: var(--muted-on-dark); }
  .contact {
    position: absolute;
    right: 46px;
    bottom: 46px;
    text-align: right;
    font-size: 19px;
    line-height: 1.45;
    list-style: none;
  }
</style>
</head>
<body>
  <section class="card card--front" aria-label="Card front">
    <div class="front-brand">
      <span class="brand-square"></span>
      <span class="brand-name">HARBORLINE</span>
    </div>
    <div class="front-tagline">Revenue Management Solutions</div>
    <div class="front-website">www.HarborlineRMS.com</div>
  </section>

  <section class="card card--back" aria-label="Card back">
    <div class="back-brand">
      <div class="brand-row">
        <span class="brand-square"></span>
        <span class="brand-name">HARBORLINE</span>
      </div>
      <div class="brand-tagline">Revenue Management Solutions</div>
    </div>
    <div class="person">
      <div class="person-name">Dana Whitfield</div>
      <div class="person-title">Regional Revenue Manager</div>
    </div>
    <ul class="contact">
      <li>Office 503-555-0148</li>
      <li>Fax 503-555-0172</li>
      <li>Dana@HarborlineRMS.com</li>
    </ul>
  </section>
</body>
</html>
```